Quiet Verses Across Winter Evenings

Need a BOOK COVER, SPINE, and BACK for above named book. This is the story of my late wife (a university professor) told through her own songs and poems. It is about the people she loved, especially her grand children, her extensive professional and life interests, her family, friends, and festivities, her illness, etc.
Updates

Need extra days to review

Target Market(s)

Family and friends

Font styles to use
Other font styles liked:
• Times New Roman

Requirements
Must have
• Regret I haven't given much thought to it...
Nice to have
• Regret I haven't given much thought to it..
Should not have

```html
<!DOCTYPE html>
<html lang="en">
<head>
<meta charset="utf-8">
<title>Quiet Verses Across Winter Evenings — Cover Wrap</title>
<link rel="stylesheet" href="https://fonts.googleapis.com/css2?family=Marcellus&family=EB+Garamond:wght@400&family=Cinzel:wght@400&display=swap">
<style>
  :root {
    --page: #f2f2f4;
    --paper: #ffffff;
    --frame: #8c88a3;
    --ink: #1c1c1c;
    --ornament: #2a2a2a;
    --mint: #dcebe3;
    --petal-soft: #ecc46a;
  }
  * { margin: 0; padding: 0; box-sizing: border-box; }
  html, body {
    width: 899px; height: 1200px; overflow: hidden;
    background: var(--page);
  }
  .cover-wrap {
    position: absolute; left: 20px; top: 302px;
    width: 858px; height: 595px;
    background: var(--paper);
    border: 2px solid var(--frame);
    box-shadow: 0 2px 6px rgba(60, 55, 90, 0.25);
    overflow: hidden;
    color: var(--ink);
  }
  .photo-layer { position: absolute; left: 0; top: 0; width: 858px; height: 595px; display: block; }

  /* back cover */
  .back-ornament { position: absolute; left: 84px; top: 46px; width: 234px; height: 34px; }
  .back-blurb {
    position: absolute; left: 53px; top: 128px; width: 298px;
    font-family: "EB Garamond", "Times New Roman", serif;
    font-size: 10.6px; line-height: 13.1px;
    text-align: justify; hyphens: auto;
  }

  /* spine */
  .spine-title {
    position: absolute; left: 429px; top: 268px;
    transform: translate(-50%, -50%) rotate(-90deg);
    white-space: nowrap;
    font-family: "Marcellus", "Times New Roman", serif;
    font-size: 15.5px; letter-spacing: 0.3px;
  }
  .spine-mark { position: absolute; left: 417px; top: 522px; width: 24px; height: 30px; }

  /* front cover */
  .author {
    position: absolute; left: 665px; top: 24px;
    transform: translateX(-50%); white-space: nowrap;
    font-family: "Cinzel", "Times New Roman", serif;
    font-size: 13px; letter-spacing: 5.2px;
  }
  .title {
    position: absolute; left: 665px; top: 446px;
    transform: translateX(-50%); white-space: nowrap;
    font-family: "Marcellus", "Times New Roman", serif;
    font-size: 35px; font-weight: 400; letter-spacing: 0.5px;
  }
  .title-ornament { position: absolute; left: 548px; top: 492px; width: 234px; height: 30px; }
  .subtitle {
    position: absolute; left: 665px; top: 538px;
    transform: translateX(-50%); white-space: nowrap;
    font-family: "Marcellus", "Times New Roman", serif;
    font-size: 22px; letter-spacing: 0.3px;
  }
</style>
</head>
<body>
  <main class="cover-wrap">
    <svg class="photo-layer" viewBox="0 0 858 595" aria-hidden="true">
      <defs>
        <linearGradient id="photoTone" x1="0" y1="0" x2="1" y2="1">
          <stop offset="0" stop-color="var(--petal-soft)"/>
          <stop offset="1" stop-color="var(--mint)"/>
        </linearGradient>
      </defs>
      <circle role="img" aria-label="Photograph: close-up of a half-open yellow sunflower bud on a pale mint background"
              cx="203" cy="503" r="203" fill="url(#photoTone)"/>
      <circle role="img" aria-label="Photograph: yellow sunflower bud on its stem against a pale mint circle"
              cx="658" cy="226" r="166" fill="url(#photoTone)"/>
    </svg>

    <svg class="back-ornament" viewBox="0 0 234 34" role="img" aria-label="Decorative scroll flourish">
      <rect x="0" y="14" width="234" height="6" rx="3" fill="var(--ornament)" opacity="0.35"/>
    </svg>

    <p class="back-blurb">Lorem ipsum dolor sit amet, consectetur adipiscing elit. Maecenas ac mattis odio, quis ullamcorper massa. Mauris interdum massa felis, sed interdum sapien volutpat quis. Nullam sagittis orci tincidunt diam viverra, eget maximus est congue. Sed sed est scelerisque, accumsan urna nec, rhoncus dui. Sed efficitur sodales purus sit amet viverra. Nullam varius pretium luctus. Integer semper eget neque at ullamcorper. Nulla pulvinar, ante a interdum tempus, turpis lacus luctus massa, ac congue purus est ut quam. In tristique nunc felis, quis ullamcorper lorem rhoncus vitae. Integer ultrices in nisl sed rhoncus. Mauris magna elit, feugiat eget dapibus et, congue at tellus.</p>

    <div class="spine-title">QUIET VERSES ACROSS WINTER EVENINGS</div>
    <svg class="spine-mark" viewBox="0 0 24 30" role="img" aria-label="Small decorative floral mark">
      <rect x="2" y="2" width="20" height="26" rx="4" fill="var(--ornament)" opacity="0.35"/>
    </svg>

    <div class="author">MIRIAM ASHFORD LANE</div>
    <h1 class="title">QUIET VERSES</h1>
    <svg class="title-ornament" viewBox="0 0 234 30" role="img" aria-label="Decorative scroll flourish">
      <rect x="0" y="12" width="234" height="6" rx="3" fill="var(--ornament)" opacity="0.35"/>
    </svg>
    <div class="subtitle">ACROSS WINTER EVENINGS</div>
  </main>
</body>
</html>
```